Tarrow Creek plumbing plumbing company business card design

Something sinilar to business card i upload it is my old business card design
And have a good watermark with the logo or majority of the logot in rhe background as watermark

Plumbing business similar to uploaded design with a nice watermark of the logo

Font styles to use
Script

Colors

Designer to choose colors to be used in the design.

```html
<!DOCTYPE html>
<html lang="en">
<head>
<meta charset="utf-8">
<title>Tarrow Creek Plumbing – Business Card</title>
<link rel="stylesheet" href="https://fonts.googleapis.com/css2?family=Montserrat:wght@400;500;600;700&display=swap">
<style>
  :root {
    --backdrop: #3a3a3c;
    --card-black: #050505;
    --card-blue: #0a78c2;
    --blue-deep: #0667ab;
    --blue-light: #2f93d6;
    --accent-blue: #1a86d0;
    --white: #ffffff;
    --soft-white: #e9eef3;
  }
  * { margin: 0; padding: 0; box-sizing: border-box; }
  html, body {
    width: 1200px; height: 1021px; overflow: hidden;
    background: var(--backdrop);
    font-family: "Montserrat", sans-serif;
  }
  .canvas { position: relative; width: 1200px; height: 1021px; }

  .card {
    position: absolute; width: 760px; height: 430px;
    border-radius: 4px; overflow: hidden;
    box-shadow: 0 18px 40px rgba(0,0,0,.45);
  }

  /* Large faint brand-name watermark */
  .watermark {
    position: absolute; white-space: nowrap;
    font-weight: 700; text-transform: uppercase;
    line-height: 1; pointer-events: none;
  }
  .card-front .watermark {
    left: 40px; top: -95px; font-size: 170px; letter-spacing: 4px;
    color: rgba(255,255,255,.07);
  }
  .card-back .watermark {
    left: -10px; bottom: -62px; font-size: 170px; letter-spacing: 4px;
    color: rgba(255,255,255,.13);
  }

  /* Front */
  .card-front { left: 330px; top: 50px; background: var(--card-black); }
  .front-brand {
    position: absolute; left: 0; right: 0; top: 170px;
    display: flex; align-items: center; justify-content: center; gap: 18px;
  }
  .brand-square { width: 30px; height: 30px; background: var(--accent-blue); flex: none; }
  .front-brand .brand-name {
    color: var(--soft-white); font-weight: 700; font-size: 40px;
    letter-spacing: 2px; text-transform: uppercase;
  }
  .front-url {
    position: absolute; left: 0; right: 0; top: 300px; text-align: center;
    font-size: 17px; letter-spacing: 5px; color: var(--accent-blue);
  }
  .front-url .tld { color: var(--soft-white); }

  /* Back */
  .card-back { left: 110px; top: 540px; background: linear-gradient(135deg, var(--blue-light) 0%, var(--card-blue) 45%, var(--blue-deep) 100%); }
  .back-brand {
    position: absolute; left: 44px; top: 44px;
    display: flex; align-items: center; gap: 12px;
  }
  .back-brand .brand-square { width: 20px; height: 20px; background: var(--white); }
  .back-brand .brand-name {
    color: var(--white); font-weight: 700; font-size: 26px;
    letter-spacing: 1.5px; text-transform: uppercase;
  }
  .contact-list { position: absolute; left: 44px; top: 160px; list-style: none; }
  .contact-list li {
    display: flex; align-items: center; gap: 10px;
    color: var(--white); font-size: 19px; line-height: 30px;
  }
  .contact-list svg { width: 16px; height: 16px; fill: none; stroke: var(--white); stroke-width: 1.6; }
  .person { position: absolute; right: 70px; top: 210px; text-align: right; color: var(--white); }
  .person .name { font-weight: 600; font-size: 25px; }
  .person .role { font-size: 18px; margin-top: 2px; }

  .licence {
    position: absolute; right: 50px; bottom: 36px; padding: 12px 30px;
    border-radius: 0 10px 10px 0; background: rgba(255,255,255,.12);
    color: var(--white); font-size: 19px; font-weight: 500;
  }
</style>
</head>
<body>
<main class="canvas">

  <section class="card card-front" aria-label="Card front">
    <span class="watermark" aria-hidden="true">Tarrow Creek</span>
    <div class="front-brand">
      <span class="brand-square"></span>
      <span class="brand-name">Tarrow Creek Plumbing</span>
    </div>
    <p class="front-url">tarrowcreekplumbing<span class="tld">.com.au</span></p>
  </section>

  <section class="card card-back" aria-label="Card back">
    <span class="watermark" aria-hidden="true">Tarrow Creek</span>
    <div class="back-brand">
      <span class="brand-square"></span>
      <span class="brand-name">Tarrow Creek Plumbing</span>
    </div>

    <ul class="contact-list">
      <li>
        <svg viewBox="0 0 16 16"><path d="M3 1.5h3l1.2 3.2-1.8 1.2a8 8 0 0 0 4.7 4.7l1.2-1.8 3.2 1.2v3a1.5 1.5 0 0 1-1.6 1.5A12.5 12.5 0 0 1 1.5 3.1 1.5 1.5 0 0 1 3 1.5z"/></svg>
        0400 555 127
      </li>
      <li>
        <svg viewBox="0 0 16 16"><rect x="1.5" y="3.5" width="13" height="9"/><path d="M1.5 3.5l6.5 5 6.5-5"/></svg>
        info@tarrowcreekplumbing.com.au
      </li>
      <li>
        <svg viewBox="0 0 16 16"><circle cx="8" cy="8" r="6.5"/><path d="M1.5 8h13M8 1.5c2.5 2.5 2.5 10.5 0 13M8 1.5c-2.5 2.5-2.5 10.5 0 13"/></svg>
        tarrowcreekplumbing.com.au
      </li>
    </ul>

    <div class="person">
      <p class="name">Dario Velmont</p>
      <p class="role">Director</p>
    </div>

    <p class="licence">Lic No. 408216c</p>
  </section>

</main>
</body>
</html>
```